Dental Business Card

I need Dental oriented business cards.
On the front side -
- on the first line, my name:
Dr Marlo Vintner
- on the second line (just underneath):
Doctor of Dental Medicine
- on the third line, or underneath that or in a corner, I would like the address and phone number:
5182 Ch. Birchfield
Montreal QC H2T 4B9
514-629-5074
- other than that i would maybe like a logo of a tooth, but i want it to be subtle and very basic!
- I would like the card to be preferably black or dark grey-ish with the writing in white
On the other side -
- 2-3 lines with the possibility to write the next appointment the box with the lines should be white, with the rest of the card being black

```html
<!DOCTYPE html>
<html lang="en">
<head>
<meta charset="UTF-8">
<title>Dr Marlo Vintner – Business Card</title>
<link href="https://fonts.googleapis.com/css2?family=Quicksand:wght@300;400;500;700&display=swap" rel="stylesheet">
<style>
  :root {
    --backdrop: #2b2b2b;
    --card: #1d1d1d;
    --ink: #e9e9e9;
    --ink-soft: #d2d2d2;
    --note-box: #ececec;
  }
  html, body {
    margin: 0;
    padding: 0;
    width: 1200px;
    height: 1200px;
    overflow: hidden;
    background: var(--backdrop);
    font-family: "Quicksand", sans-serif;
    color: var(--ink);
  }
  .canvas {
    position: relative;
    width: 1200px;
    height: 1200px;
  }
  .card {
    position: absolute;
    left: 228px;
    width: 744px;
    height: 424px;
    background: var(--card);
    border-radius: 32px;
    box-shadow: 0 10px 26px rgba(0,0,0,0.45);
  }
  .card--front { top: 136px; }
  .card--back { top: 640px; }

  .brand {
    position: absolute;
    left: 0;
    right: 0;
    display: flex;
    justify-content: center;
    align-items: center;
    gap: 14px;
  }
  .card--front .brand { top: 90px; }
  .card--back .brand { top: 74px; }
  .brand__circle {
    width: 34px;
    height: 34px;
    border: 3px solid var(--ink);
    border-radius: 50%;
    box-sizing: border-box;
  }
  .brand__name {
    font-weight: 500;
    font-size: 28px;
    letter-spacing: 0.5px;
    color: var(--ink);
  }

  .identity {
    position: absolute;
    top: 180px;
    left: 0;
    right: 0;
    text-align: center;
  }
  .identity__name {
    margin: 0;
    font-weight: 700;
    font-size: 32px;
    line-height: 40px;
  }
  .identity__title {
    margin: 0;
    font-weight: 400;
    font-size: 22px;
    line-height: 30px;
    letter-spacing: 0.6px;
    color: var(--ink-soft);
  }

  .contact {
    position: absolute;
    top: 322px;
    font-weight: 400;
    font-size: 19px;
    line-height: 27px;
    letter-spacing: 0.4px;
    color: var(--ink-soft);
  }
  .contact--address { left: 34px; }
  .contact--reach { right: 34px; text-align: right; top: 320px; }
  .contact p { margin: 0; }

  .appointment-box {
    position: absolute;
    left: 34px;
    top: 182px;
    width: 676px;
    height: 144px;
    background: var(--note-box);
    border-radius: 28px;
  }
  .policy-note {
    position: absolute;
    left: 0;
    right: 0;
    top: 340px;
    margin: 0;
    text-align: center;
    font-weight: 500;
    font-size: 17px;
    line-height: 22px;
    letter-spacing: 0.3px;
    color: var(--ink-soft);
  }
</style>
</head>
<body>
<div class="canvas">

  <section class="card card--front">
    <div class="brand">
      <span class="brand__circle"></span>
      <span class="brand__name">Vintner Dental</span>
    </div>
    <div class="identity">
      <h1 class="identity__name">Dr Marlo Vintner</h1>
      <p class="identity__title">Doctor of Dental Medicine</p>
    </div>
    <div class="contact contact--address">
      <p>5182 Ch. Birchfield</p>
      <p>Montreal QC H2T 4B9</p>
    </div>
    <div class="contact contact--reach">
      <p>514-629-5074</p>
      <p>marlovintner@mailbox.com</p>
    </div>
  </section>

  <section class="card card--back">
    <div class="brand">
      <span class="brand__circle"></span>
      <span class="brand__name">Vintner Dental</span>
    </div>
    <div class="appointment-box"></div>
    <p class="policy-note">We value your time and that of other guests and a 24 hr notice<br>is reqired if you are not able to keep your appointment</p>
  </section>

</div>
</body>
</html>
```